4D Hush Little Nest Luxury Ultrasound Billboard

Design a HIGH-END, MODERN billboard for my private prenatal ultrasound studio, 4D Hush Little Nest, located in Pace, Florida.
This billboard will be viewed by drivers traveling at highway speeds, so it must be extremely clean, simple, and readable within 6 seconds.
About My Business
4D Hush Little Nest is a private prenatal ultrasound studio specializing in:
Highest technology 4D/HD Ultrasounds
Early Gender Determination
Pregnancy Confirmation
I have been serving families for nearly 10 years and is known for creating a memorable experience, not just an ultrasound appointment.
Design Style
I DO NOT want:
Flowers
Leaves
Swirls
Glitter
Hearts everywhere
Busy backgrounds
Generic maternity stock graphics
I DO want:
Modern
Luxury
Upscale
Clean
Professional
Eye-catching
Premium medical spa feel
Colors
Use colors from my logo:
LOGO Green ( or a deep green)
Black
White
Soft Gold accents
Images:
Incorporate my professional headshot in a clean, modern way, logo, and the ultrasound images
Text
Keep wording minimal.
Primary Headline ( OPEN TO IDEAS) :
EXAMPLES ( WOULD RATHER SOMETHING MORE CATCHY)
" ADVANCED IMAGING. UNFORGETTABLE MOMENTS"
"MEET YOUR BABY BEFORE BIRTH"
Under headline:
4D Ultrasound • Early Gender • Pregnancy Confirmation
Business Name:
4D Hush Little Nest
Private Prenatal Ultrasound Studio
Phone Number:
850-471-3905
Important
This billboard must be readable in 5–6 seconds from a moving vehicle.
Less text is better.
The phone number and business name must be visible from a distance.
The design should feel like a premium brand that immediately tells expecting parents:
“This is where I go to see my baby.”
Files Provided
Official logo
Headshot
Ultrasound images
Don’t make this look like a medical office billboard.
Make it look like a luxury baby experience billboard. That’s what separates 4D Hush Little Nest from hospitals, OB offices, and all the new studios popping up around you. The emotional connection is what gets moms to book. ❤️
Billboard Size - 10.6” x 36”

```html
<!DOCTYPE html>
<html lang="en">
<head>
<meta charset="utf-8">
<title>4D Hush Little Nest – Billboard</title>
<link href="https://fonts.googleapis.com/css2?family=Roboto+Condensed:wght@600;700&family=Montserrat:wght@500&family=Mrs+Saint+Delafield&display=swap" rel="stylesheet">
<style>
  :root {
    --green: #4f625a;
    --gold: #c4963a;
    --black: #0b0b0b;
    --white: #ffffff;
    --page: #e4e3e3;
    --scan: #8c4a3c;
    --scan-dark: #5a2a22;
    --portrait: #3a3a36;
  }
  html, body {
    margin: 0;
    width: 1200px;
    height: 1080px;
    overflow: hidden;
    background: var(--page);
  }
  .billboard {
    position: absolute;
    left: 30px;
    top: 374px;
    width: 1140px;
    height: 332px;
    background: var(--white);
    overflow: hidden;
    font-family: "Roboto Condensed", sans-serif;
  }
  .brand {
    position: absolute;
    left: 40px;
    top: 28px;
    width: 282px;
    text-align: center;
  }
  .brand-name {
    margin: 0;
    color: var(--gold);
    font-weight: 700;
    font-size: 42px;
    line-height: 44px;
  }
  .brand-tagline {
    margin: 14px 0 0;
    font-family: "Montserrat", sans-serif;
    font-weight: 500;
    font-size: 12.5px;
    letter-spacing: 0.6px;
    color: var(--green);
    white-space: nowrap;
  }
  .divider {
    position: absolute;
    left: 338px;
    top: 18px;
    width: 3px;
    height: 148px;
    background: var(--green);
  }
  .headline {
    position: absolute;
    left: 350px;
    top: 10px;
    margin: 0;
    color: var(--green);
    font-weight: 700;
    font-size: 46px;
    line-height: 41px;
    letter-spacing: 0.5px;
    white-space: nowrap;
  }
  .headline-script {
    position: absolute;
    left: 362px;
    top: 94px;
    margin: 0;
    font-family: "Mrs Saint Delafield", cursive;
    font-size: 84px;
    line-height: 78px;
    color: var(--gold);
    font-weight: 400;
    white-space: nowrap;
  }
  .scan-frame {
    position: absolute;
    left: 696px;
    top: 95px;
    width: 110px;
    height: 134px;
    background: var(--black);
    border-radius: 6px;
  }
  .scan-image {
    position: absolute;
    left: 6px;
    top: 7px;
    right: 6px;
    bottom: 9px;
    background: radial-gradient(circle at 50% 45%, var(--scan), var(--scan-dark));
  }
  .services {
    position: absolute;
    top: 186px;
    left: 44px;
    display: flex;
    gap: 6px;
  }
  .service {
    box-sizing: border-box;
    height: 45px;
    padding: 0 12px;
    border: 3px solid var(--green);
    color: var(--gold);
    font-weight: 600;
    font-size: 22px;
    display: flex;
    align-items: center;
    justify-content: center;
    white-space: nowrap;
  }
  .contact-band {
    position: absolute;
    left: 0;
    right: 0;
    top: 243px;
    height: 89px;
    background: var(--black);
  }
  .contact-row {
    position: absolute;
    left: 42px;
    top: 243px;
    height: 89px;
    width: 770px;
    display: flex;
    align-items: center;
    gap: 16px;
    white-space: nowrap;
  }
  .phone {
    color: var(--white);
    font-weight: 700;
    font-size: 54px;
    letter-spacing: -1px;
  }
  .contact-divider {
    width: 3px;
    height: 46px;
    background: var(--white);
    flex: none;
  }
  .website {
    color: var(--gold);
    font-weight: 700;
    font-size: 46px;
  }
  .film-strip {
    position: absolute;
    left: 821px;
    top: 0;
    width: 292px;
    height: 332px;
  }
  .portrait {
    position: absolute;
    left: 869px;
    top: 27px;
    width: 196px;
    height: 276px;
    border-radius: 14px;
    background: linear-gradient(180deg, var(--black) 0%, var(--portrait) 100%);
  }
</style>
</head>
<body>
  <section class="billboard">
    <div class="brand">
      <h1 class="brand-name">4D Hush<br>Little Nest</h1>
      <p class="brand-tagline">PRENATAL ULTRASOUND STUDIO</p>
    </div>

    <div class="divider"></div>

    <h2 class="headline">ADVANCED IMAGING.<br>UNFORGETTABLE</h2>
    <p class="headline-script">Moments</p>

    <div class="scan-frame">
      <div class="scan-image" role="img" aria-label="4D ultrasound image of twin babies face to face"></div>
    </div>

    <div class="services">
      <div class="service">4D ULTRASOUND</div>
      <div class="service">EARLY GENDER</div>
      <div class="service">PREGNANCY CONFIRMATION</div>
    </div>

    <div class="contact-band"></div>
    <div class="contact-row">
      <div class="phone">850-471-3905</div>
      <div class="contact-divider"></div>
      <div class="website">4dhushlittlenest.com</div>
    </div>

    <svg class="film-strip" viewBox="0 0 292 332" aria-hidden="true">
      <rect x="0" y="0" width="292" height="332" fill="var(--gold)"/>
      <rect x="48" y="-6" width="196" height="14" rx="5" fill="var(--white)"/>
      <rect x="48" y="324" width="196" height="14" rx="5" fill="var(--white)"/>
      <g fill="var(--white)">
        <rect x="13" y="10" width="24" height="22" rx="4"/>
        <rect x="13" y="53" width="24" height="22" rx="4"/>
        <rect x="13" y="96" width="24" height="22" rx="4"/>
        <rect x="13" y="139" width="24" height="22" rx="4"/>
        <rect x="13" y="182" width="24" height="22" rx="4"/>
        <rect x="13" y="225" width="24" height="22" rx="4"/>
        <rect x="13" y="268" width="24" height="22" rx="4"/>
        <rect x="13" y="311" width="24" height="22" rx="4"/>
        <rect x="255" y="10" width="24" height="22" rx="4"/>
        <rect x="255" y="53" width="24" height="22" rx="4"/>
        <rect x="255" y="96" width="24" height="22" rx="4"/>
        <rect x="255" y="139" width="24" height="22" rx="4"/>
        <rect x="255" y="182" width="24" height="22" rx="4"/>
        <rect x="255" y="225" width="24" height="22" rx="4"/>
        <rect x="255" y="268" width="24" height="22" rx="4"/>
        <rect x="255" y="311" width="24" height="22" rx="4"/>
      </g>
    </svg>
    <div class="portrait" role="img" aria-label="Professional headshot of the studio owner holding an ultrasound probe"></div>
  </section>
</body>
</html>
```